Wren's Home Care Retractable Banner Design

Retractable Banner Design
We need a pull up retractable banner design
85 x 206 cm.
We need the banner to use at expo's, information sessions, presentations, recruitment days. Needs to be attractive to our elderly client's and staff (care workers)
Phone number needs to be on 08 7394 2650
Website also needs to be on the banner : wrenshomecare-example.com.au

Target Market(s)

35 +

Industry/Entity Type

aged care / community

Requirements
Must have
• Colours, fonts and logo as detailed in upload

```html
<!DOCTYPE html>
<html lang="en">
<head>
<meta charset="utf-8">
<title>Wren's Home Care – Pull Up Banner</title>
<link rel="stylesheet" href="https://fonts.googleapis.com/css2?family=Poppins:ital,wght@0,400;0,500;0,600;1,700&family=Allura&display=swap">
<style>
  :root {
    --maroon: #8c1a2c;
    --paper: #ffffff;
    --backdrop: #eeebe8;
    --photo-light: #e6d6d0;
    --photo-mid: #b9868a;
    --photo-dark: #8c1a2c;
  }
  * { margin: 0; padding: 0; box-sizing: border-box; }
  html, body {
    width: 1200px;
    height: 800px;
    overflow: hidden;
    background: var(--backdrop);
  }
  .canvas {
    position: relative;
    width: 1200px;
    height: 800px;
  }
  .banner {
    position: absolute;
    left: 445px;
    top: 25px;
    width: 310px;
    height: 750px;
    background: var(--paper);
    overflow: hidden;
    box-shadow: 0 2px 10px rgba(0,0,0,0.08);
  }
  .banner-shapes {
    position: absolute;
    inset: 0;
  }
  .brand {
    position: absolute;
    top: 58px;
    left: 0;
    width: 100%;
    text-align: center;
    font-family: 'Poppins', sans-serif;
    font-weight: 500;
    font-size: 25px;
    line-height: 1;
    color: var(--maroon);
  }
  .headline {
    position: absolute;
    top: 448px;
    left: 0;
    width: 100%;
    text-align: center;
    color: var(--maroon);
    font-weight: normal;
  }
  .headline-lead {
    font-family: 'Poppins', sans-serif;
    font-style: italic;
    font-weight: 700;
    font-size: 33px;
    line-height: 1.1;
    letter-spacing: -0.3px;
  }
  .headline-mid {
    font-family: 'Poppins', sans-serif;
    font-weight: 400;
    font-size: 20px;
    line-height: 1.25;
    margin-left: 40px;
  }
  .headline-script {
    font-family: 'Allura', cursive;
    font-weight: 400;
    font-size: 50px;
    line-height: 0.85;
  }
  .headline-script.second { margin-right: 30px; }
  .contact {
    position: absolute;
    top: 662px;
    left: 0;
    width: 100%;
    display: flex;
    flex-direction: column;
    align-items: center;
  }
  .phone-pill {
    background: var(--maroon);
    color: var(--paper);
    font-family: 'Poppins', sans-serif;
    font-weight: 500;
    font-size: 27px;
    line-height: 1;
    padding: 9px 16px 8px;
    border-radius: 12px;
    width: 250px;
    text-align: center;
  }
  .website {
    margin-top: 10px;
    font-family: 'Poppins', sans-serif;
    font-weight: 600;
    font-size: 13.5px;
    color: var(--maroon);
  }
</style>
</head>
<body>
<main class="canvas">
  <section class="banner">
    <svg class="banner-shapes" viewBox="0 0 310 750" width="310" height="750">
      <defs>
        <linearGradient id="photoTone" x1="0" y1="0" x2="1" y2="1">
          <stop offset="0" stop-color="#8c1a2c"/>
          <stop offset="0.45" stop-color="#b9868a"/>
          <stop offset="1" stop-color="#e6d6d0"/>
        </linearGradient>
      </defs>
      <path class="photo-area" role="img"
            aria-label="Photo of a smiling carer in a maroon uniform embracing an elderly woman in glasses, set against a large maroon petal shape"
            d="M0 130 H310 V392 Q155 352 0 392 Z" fill="url(#photoTone)"/>
      <path class="band-arc-top" d="M0 404 Q155 362 310 404" fill="none" stroke="#8c1a2c" stroke-width="1.5"/>
      <path class="band-arc-bottom" d="M0 618 Q155 660 310 618" fill="none" stroke="#8c1a2c" stroke-width="1.5"/>
    </svg>

    <header class="brand">Wren's Home Care</header>

    <h1 class="headline">
      <span class="headline-lead">Every Senior</span><br>
      <span class="headline-mid">Deserves</span><br>
      <span class="headline-script">Respect &amp;</span><br>
      <span class="headline-script second">love</span>
    </h1>

    <footer class="contact">
      <span class="phone-pill">08 7394 2650</span>
      <span class="website">wrenshomecare-example.com.au</span>
    </footer>
  </section>
</main>
</body>
</html>
```